Design Invitation using a mobile phone screen image

This invitation is for 12 year olds finishing primary school so make it fun and bright.
Invitation should be an kavlet with a text message saying.....
Dress in your best (insert emoticons - boy in long pants/girl in dress) for your Year 6 farewell dinner (insert emoticon with tear) on Monday 12 December at 6 pm (insert emoticons - party hat, thumbs up and bowl of icecream). Going 2b a gr8 night!
rsvp YES PLEASE and your name to 0517XXXXXXX

Target Market(s)

12/13 years old boys and girls

Industry/Entity Type

School

Requirements
Must have
• Must be bright and look like a text message - it can have an artwork within it as if the invite has been texted and then a comment is made after the image.
• Must us an kavlet screen as the invitation but so we dont have to cut it out it can be a rectanglar card

```html
<!DOCTYPE html>
<html lang="en">
<head>
<meta charset="utf-8">
<title>Year 6 Farewell Dinner Invitation</title>
<link rel="stylesheet" href="https://fonts.googleapis.com/css2?family=Varela+Round&display=swap">
<style>
  :root {
    --page-top: #ececec;
    --page-bottom: #f7f7f7;
    --page-white: #ffffff;
    --card-blue: #8ed4e8;
    --confetti-pink: #ef5f86;
    --confetti-teal: #35c2b4;
    --confetti-yellow: #f2e27a;
    --phone-body: #545454;
    --phone-bezel: #3f3f3f;
    --phone-glare: #6a6a6a;
    --screen: #ffffff;
    --bubble-green: #c3d644;
    --bubble-grey: #e2e2e2;
    --bubble-edge: #ffffff;
    --ink-green: #5a4a72;
    --ink-grey: #4f4f58;
    --icon-clothes: #f4b4c8;
    --icon-party: #b98bd0;
    --icon-face: #d9d9d9;
  }
  * { box-sizing: border-box; margin: 0; padding: 0; }
  html, body { width: 1200px; height: 1002px; overflow: hidden; }
  body {
    position: relative;
    background: var(--page-white);
    font-family: "Varela Round", Arial, sans-serif;
  }
  .backdrop {
    position: absolute; left: 0; top: 0; width: 1200px; height: 866px;
    background: linear-gradient(180deg, var(--page-top), var(--page-bottom));
  }
  .card {
    position: absolute; left: 82px; top: 65px; width: 1053px; height: 708px;
    background: var(--card-blue);
    overflow: hidden;
  }
  .confetti {
    position: absolute; left: 0; top: 0; width: 100%; height: 420px;
    background:
      radial-gradient(ellipse 60% 70% at 15% 0%, rgba(239,95,134,.45), transparent 70%),
      radial-gradient(ellipse 50% 60% at 50% 0%, rgba(242,226,122,.55), transparent 70%),
      radial-gradient(ellipse 60% 70% at 85% 0%, rgba(53,194,180,.45), transparent 70%);
  }
  .phone {
    position: absolute; left: 305px; top: 61px; width: 443px; height: 700px;
  }
  .bubble {
    position: absolute;
    border: 3px solid var(--bubble-edge);
    border-radius: 16px;
    font-size: 19px;
    line-height: 1.2;
    padding: 14px 16px;
  }
  .bubble::before, .bubble::after {
    content: ""; position: absolute; width: 0; height: 0;
  }
  .bubble--incoming { background: var(--bubble-grey); color: var(--ink-grey); }
  .bubble--incoming::before {
    left: 6px; bottom: -22px;
    border-top: 22px solid var(--bubble-edge);
    border-right: 22px solid transparent;
  }
  .bubble--incoming::after {
    left: 9px; bottom: -16px;
    border-top: 17px solid var(--bubble-grey);
    border-right: 16px solid transparent;
  }
  .bubble--outgoing { background: var(--bubble-green); color: var(--ink-green); text-align: center; }
  .bubble--outgoing::before {
    right: 6px; bottom: -22px;
    border-top: 22px solid var(--bubble-edge);
    border-left: 22px solid transparent;
  }
  .bubble--outgoing::after {
    right: 9px; bottom: -16px;
    border-top: 17px solid var(--bubble-green);
    border-left: 16px solid transparent;
  }
  .dress-code { left: 673px; top: 131px; width: 165px; height: 79px; text-align: center; }
  .occasion   { left: 212px; top: 234px; width: 204px; height: 97px; }
  .date-time  { left: 596px; top: 331px; width: 204px; height: 98px; padding-left: 34px; }
  .reply      { left: 229px; top: 511px; width: 204px; height: 98px; }
  .sign-off   { left: 663px; top: 543px; width: 167px; height: 80px; text-align: center; }

  .emoticon { position: absolute; border-radius: 10px; }
  .emoticon--outfits { left: 567px; top: 188px; width: 90px; height: 70px;
    background: linear-gradient(90deg, var(--phone-bezel) 0 45%, var(--icon-clothes) 55% 100%); }
  .emoticon--tear { left: 435px; top: 324px; width: 39px; height: 39px; border-radius: 50%;
    background: var(--icon-face); }
  .emoticon--party { left: 490px; top: 401px; width: 101px; height: 95px;
    background: linear-gradient(160deg, var(--icon-party), var(--confetti-teal) 55%, #c89a5a); }
</style>
</head>
<body>
  <div class="backdrop"></div>
  <main class="card">
    <div class="confetti" role="img" aria-label="Colourful confetti falling from the top of the card"></div>

    <svg class="phone" viewBox="0 0 443 700" aria-hidden="true">
      <path d="M0 90 Q0 0 90 0 H353 Q443 0 443 90 V700 H0 Z" fill="var(--phone-body)"/>
      <path d="M14 92 Q14 14 92 14 H351 Q429 14 429 92 V95 H14 Z" fill="var(--phone-bezel)"/>
      <path d="M200 14 H351 Q429 14 429 92 V95 H240 Z" fill="var(--phone-glare)"/>
      <circle cx="158" cy="58" r="6" fill="#2e2e2e"/>
      <rect x="192" y="54" width="60" height="8" rx="4" fill="#2e2e2e"/>
      <rect x="18" y="95" width="407" height="605" fill="var(--screen)"/>
    </svg>

    <div class="bubble bubble--incoming dress-code">Dress in<br>your best</div>
    <div class="emoticon emoticon--outfits" role="img" aria-label="Emoticons of a boy's long pants outfit and a girl's pink dress"></div>

    <div class="bubble bubble--outgoing occasion">For your Year 6<br>farewell dinner</div>
    <div class="emoticon emoticon--tear" role="img" aria-label="Emoticon with a tear"></div>

    <div class="bubble bubble--incoming date-time" style="text-align:left">on Monday<br>12 December<br>at 6 pm</div>
    <div class="emoticon emoticon--party" role="img" aria-label="Emoticons of party hats and a bowl of ice cream"></div>

    <div class="bubble bubble--outgoing reply">rsvp YES PLEASE<br>and your name<br>to 0517XXXXXXX</div>

    <div class="bubble bubble--incoming sign-off">Going 2b<br>a gr8 night!</div>
  </main>
</body>
</html>
```